Criação de Folder para Alimentos & Bebidas
A empresa queria:
" importamos produtos com nossas marcas e distribuimos para supermercdos e distribuidores "

```html
<!DOCTYPE html>
<html lang="pt-BR">
<head>
<meta charset="utf-8">
<title>Quorvane Foods – Folder</title>
<link rel="stylesheet" href="https://fonts.googleapis.com/css2?family=Roboto:ital,wght@0,400;0,500;0,700;1,500&display=swap">
<style>
  :root {
    --bg: #e9e6e2;
    --panel: #0d0d0d;
    --yellow: #f2c21b;
    --orange: #e87a1d;
    --red: #c4161c;
    --white: #ffffff;
    --grey: #bdbdbd;
    --meat-dark: #5a1d14;
    --meat-mid: #a8353a;
    --board: #7a4a26;
  }
  * { margin: 0; padding: 0; box-sizing: border-box; }
  html, body { width: 1200px; height: 1200px; overflow: hidden; background: var(--bg); }
  body { font-family: "Roboto", Arial, sans-serif; }
  .folder {
    position: absolute; left: 60px; top: 220px;
    width: 1080px; height: 760px;
    display: flex;
    box-shadow: 0 10px 30px rgba(0,0,0,.25);
  }
  .panel { position: relative; width: 540px; height: 760px; background: var(--panel); overflow: hidden; }
  .panel svg.shapes { position: absolute; inset: 0; }
  .brand {
    position: absolute; font-weight: 500; color: var(--white);
    display: flex; align-items: center; gap: 10px; white-space: nowrap;
  }
  .brand-dot { width: 12px; height: 12px; border-radius: 50%; background: var(--orange); }
  .front .brand { top: 34px; left: 0; right: 0; justify-content: center; font-size: 34px; }
  .back .brand { top: 430px; left: 150px; font-size: 34px; }
  .website {
    position: absolute; color: var(--white); font-weight: 700; font-size: 18px; letter-spacing: .3px;
  }
  .front .website { bottom: 32px; left: 0; right: 0; text-align: center; }
  .back .website { bottom: 60px; left: 170px; }
  .contact { position: absolute; top: 268px; left: 150px; color: var(--grey); font-size: 11.5px; line-height: 1.45; }
  .contact-title { color: var(--yellow); font-style: italic; font-weight: 500; font-size: 15px; margin-bottom: 8px; }
  .contact-row { display: flex; align-items: flex-start; gap: 10px; margin-bottom: 7px; }
  .contact-row svg { flex: none; margin-top: 1px; }
</style>
</head>
<body>
<main class="folder">

  <section class="panel back">
    <svg class="shapes" viewBox="0 0 540 760" width="540" height="760">
      <path d="M0 40 Q200 0 540 0 L0 0 Z" fill="var(--red)"/>
      <path d="M0 58 Q220 18 540 14 L540 0 Q200 0 0 40 Z" fill="var(--yellow)"/>
      <path d="M0 58 Q220 18 540 14 L540 22 Q230 28 0 66 Z" fill="var(--orange)"/>
      <path d="M0 640 Q300 690 540 620 L540 760 L0 760 Z" fill="var(--white)"/>
      <path d="M0 652 Q300 700 540 632 L540 760 L0 760 Z" fill="var(--panel)"/>
      <rect x="0" y="728" width="540" height="16" fill="var(--yellow)"/>
      <rect x="0" y="744" width="540" height="16" fill="var(--red)"/>
    </svg>

    <div class="contact">
      <p class="contact-title">Fale Conosco</p>
      <div class="contact-row">
        <svg width="16" height="16" viewBox="0 0 16 16"><path d="M8 1a5 5 0 0 0-5 5c0 4 5 9 5 9s5-5 5-9a5 5 0 0 0-5-5zm0 7a2 2 0 1 1 0-4 2 2 0 0 1 0 4z" fill="var(--yellow)"/></svg>
        <p>R. das Acácias, Nº 210<br>Centro / Cidade UF<br>CEP 11040-000</p>
      </div>
      <div class="contact-row">
        <svg width="16" height="16" viewBox="0 0 16 16"><path d="M4 2l2 3-1.5 1.5a8 8 0 0 0 5 5L11 10l3 2-1 3c-6 0-11-5-11-11z" fill="var(--yellow)"/></svg>
        <p>(12) 3456-7100 / (12) 99812-4400</p>
      </div>
      <div class="contact-row">
        <svg width="16" height="16" viewBox="0 0 16 16"><rect x="1" y="3" width="14" height="10" rx="1" fill="var(--yellow)"/><path d="M1.5 3.5 8 9l6.5-5.5" fill="none" stroke="var(--panel)" stroke-width="1.3"/></svg>
        <p>contato@quorvanefoods.com.br</p>
      </div>
    </div>

    <p class="brand"><span>Quorvane Foods</span><span class="brand-dot"></span></p>
    <p class="website">www.quorvanefoods.com.br</p>
  </section>

  <section class="panel front">
    <svg class="shapes" viewBox="0 0 540 760" width="540" height="760">
      <defs>
        <linearGradient id="meatFill" x1="0" y1="0" x2="1" y2="1">
          <stop offset="0" stop-color="var(--board)"/>
          <stop offset=".45" stop-color="var(--meat-mid)"/>
          <stop offset="1" stop-color="var(--meat-dark)"/>
        </linearGradient>
      </defs>
      <path d="M0 140 Q260 150 540 96 L540 680 L0 680 Z" fill="url(#meatFill)" role="img" aria-label="Fotografia de peça de carne bovina fatiada sobre tábua de madeira com ramo de alecrim"/>
      <path d="M0 118 Q260 124 540 70 L540 86 Q260 140 0 132 Z" fill="var(--red)"/>
      <path d="M0 132 Q260 140 540 86 L540 100 Q260 154 0 144 Z" fill="var(--yellow)"/>
      <path d="M0 672 Q280 700 540 650 L540 664 Q280 714 0 686 Z" fill="var(--orange)"/>
      <path d="M0 686 Q280 714 540 664 L540 680 Q280 728 0 700 Z" fill="var(--yellow)"/>
      <path d="M0 700 Q280 728 540 680 L540 760 L0 760 Z" fill="var(--panel)"/>
      <rect x="0" y="748" width="540" height="12" fill="var(--white)"/>
    </svg>
    <p class="brand"><span>Quorvane Foods</span><span class="brand-dot"></span></p>
    <p class="website">www.quorvanefoods.com.br</p>
  </section>

</main>
</body>
</html>
```